Corporate flyer highlighting service offering for PR agency

A corporate flyer is needed for a new service offering that we are doing. The product name is SaleNimbus it is a marketing and communications services offering for companies who are getting ready to sell their business. If we are really happy with the designer's work, there will be a great deal more projects. I am looking for a clean design with a few pops of color from my site. https://brightmoorlane.partners. I am looking for a good design with data in sections. I am looking for a clean design that feels high-end but not cluttered. Please do not use images of people. Please see the following examples of types of designs I like.
https://www.pinboardia.example/pin/830172649205518834/
https://www.pinboardia.example/pin/391827465019283745/
https://assets.tovarnel.example/corporate-flyer-template-KQPMRT
https://artbrookly.example/item/corporate-flyer-template/48193726?s_rank=8
https://assets.tovarnel.example/corporate-business-flyer-template-83VN2L
Updates

I had to place the project on hold as I choose the wrong type of project and did not get many designs as a result. I am reposting this with an updated brief.

Target Market(s)

Business sellers and brokers

Industry/Entity Type

Marketing for business sellers

Font styles to use
Sans Serif

Requirements
Must have
• Good quality design with content in sections. Clean and high end feeling is a must.
Should not have
• A lot of images of people.

```html
<!DOCTYPE html>
<html lang="en">
<head>
<meta charset="utf-8">
<title>SaleNimbus – Brightmoor Lane Partners</title>
<link href="https://fonts.googleapis.com/css2?family=Montserrat:ital,wght@0,400;0,500;0,600;0,700;0,800;1,500;1,600;1,700&family=Poppins:wght@400;500&display=swap" rel="stylesheet">
<style>
:root{
  --bg:#c9c9cb;
  --paper:#ffffff;
  --ink:#1f2328;
  --body:#3a3f45;
  --orange:#f15a24;
  --amber:#f7a21b;
  --blue:#1f7fc9;
  --blue-dark:#1565a8;
  --green:#5aa83c;
  --navy:#1e2c37;
  --navy-2:#243542;
  --grey-box:#ececec;
}
*{box-sizing:border-box;margin:0;padding:0}
html,body{width:1200px;height:4000px;overflow:hidden}
body{background:var(--bg);font-family:"Montserrat",sans-serif;color:var(--body);position:relative}
.page{position:absolute;background:var(--paper);box-shadow:0 4px 14px rgba(0,0,0,.18);overflow:hidden}
.page-one{left:197px;top:241px;width:801px;height:1133px}
.page-two{left:210px;top:1447px;width:779px;height:1102px}
.page-three{left:200px;top:2647px;width:792px;height:1117px}
.abs{position:absolute}
.brand{position:absolute;display:flex;align-items:center;gap:10px}
.brand-mark{width:18px;height:18px;background:var(--orange)}
.brand-name{font-weight:600;font-size:17px;letter-spacing:.5px;color:var(--ink);text-transform:uppercase;line-height:1.15;width:170px}
.photo{position:absolute}
p.copy{font-size:10.4px;line-height:1.32;color:var(--body)}
.hero-title{position:absolute;left:51px;top:122px;font-weight:800;font-size:46px;line-height:.9;color:var(--ink);letter-spacing:-.5px}
.hero-title .accent{color:var(--orange)}
.hero-sub{position:absolute;left:51px;top:258px;font-weight:800;font-size:18.5px;line-height:1.28;color:var(--ink)}
.hero-sub .blue{color:var(--blue)}
.rule-orange{position:absolute;left:0;top:386px;width:380px;height:4px;background:var(--amber)}
.quote-box{position:absolute;background:var(--blue);border-radius:14px;color:#fff;font-size:10.6px;line-height:1.3;padding:0 18px}
.quote-box .q-cite{font-style:italic;font-weight:600;margin-top:12px}
.quote-icon{position:absolute;width:46px;height:46px;border-radius:50%;background:var(--green);border:3px solid #fff;color:#fff;font-weight:800;font-size:34px;line-height:52px;text-align:center}
.orange-box{position:absolute;background:var(--amber);border-radius:14px;color:#fff;font-size:10px;line-height:1.3;padding:16px 16px}
.deal-types{position:absolute;left:414px;top:600px;width:340px;display:flex}
.deal{flex:1;text-align:center;font-size:9.6px;font-weight:700;color:var(--ink);line-height:1.15;border-right:1px solid #bfc4c9;padding:0 2px}
.deal:last-child{border-right:0}
.deal svg{display:block;margin:0 auto 6px}
.divider{position:absolute;height:1px;background:#bfc4c9}
.value-title{position:absolute;left:0;width:100%;text-align:center;font-weight:700;font-size:17px;color:var(--ink)}
.value-row{position:absolute;left:64px;top:961px;width:686px;height:97px;display:flex}
.value-cell{flex:1;background:var(--navy);position:relative;color:#fff;font-size:10.8px;font-weight:500;line-height:1.25;text-align:center;padding-top:44px}
.value-cell:nth-child(2n){background:var(--navy-2)}
.value-badge{position:absolute;left:50%;top:-32px;width:58px;height:58px;margin-left:-29px}
.footer{position:absolute;left:0;width:100%;display:flex;justify-content:center;align-items:center;gap:14px;font-family:"Poppins",sans-serif;font-size:16px;color:var(--ink)}
.footer .sep{color:#555}
.footer .item{display:flex;align-items:center;gap:7px}
.banner-text{position:absolute;left:298px;top:48px;width:440px;color:#fff;font-size:11.4px;font-weight:500;line-height:1.3}
.section-head{position:absolute;font-weight:700;font-size:16.5px}
.section-head.blue{color:var(--blue)}
.section-head.orange{color:var(--orange)}
.checks{position:absolute;list-style:none}
.checks li{position:relative;padding-left:17px;font-size:10px;line-height:1.28;margin-bottom:8px}
.checks li::before{content:"✓";position:absolute;left:0;top:0;width:10px;height:10px;border:1px solid var(--green);border-radius:50%;color:var(--green);font-size:7px;line-height:10px;text-align:center}
.checks li b{display:block;color:var(--green);font-size:13px;margin-left:-17px;padding-left:17px}
.checks.bold li{font-weight:600;color:var(--ink);margin-bottom:7px}
.stat-box{position:absolute;left:51px;top:372px;width:678px;height:140px;background:var(--orange);border-radius:16px;color:#fff}
.stat{position:absolute;width:52px;height:52px;border-radius:50%;background:#fff;border:4px solid var(--green);color:var(--ink);text-align:center;font-weight:800;font-size:19px;line-height:1}
.stat span{display:block;font-size:6px;font-weight:500;margin-top:2px}
.stat-text{position:absolute;left:200px;width:460px;font-size:10.2px;line-height:1.3}
.icon-tile{position:absolute;width:36px;height:36px;border-radius:7px}
.dotted{position:absolute;border-left:2px dotted #9aa3ab}
.grey-box{position:absolute;left:51px;top:209px;width:698px;height:108px;background:var(--grey-box);border-radius:16px;padding:12px 18px}
.grey-box h3{color:var(--blue);font-style:italic;font-weight:700;font-size:16px;margin-bottom:4px}
.lead-blue{position:absolute;left:425px;top:344px;width:322px;color:var(--blue);font-style:italic;font-weight:500;font-size:13px;line-height:1.22}
.product h4{position:absolute;color:var(--blue);font-weight:500;font-size:15px}
.note{position:absolute;left:51px;width:698px;font-size:10.2px;line-height:1.3}
.note b{color:var(--orange);font-weight:700}
.note em{color:var(--orange);font-style:normal}
.dots{position:absolute;left:51px;width:698px;border-top:1.5px dotted #8c939a}
</style>
</head>
<body>

<section class="page page-one">
  <div class="brand" style="left:51px;top:52px"><span class="brand-mark"></span><span class="brand-name">Brightmoor Lane Partners</span></div>

  <h1 class="hero-title"><span class="accent">SALENIMBUS</span><br>PROVIDES<br>EXECUTIVES</h1>
  <p class="hero-sub"><span class="blue">AND BUSINESS OWNERS WITH<br>CLEAR GUIDANCE</span> TO UNLOCK<br>NON-FINANCIAL VALUE<br>AHEAD OF AN EXIT.</p>

  <svg class="photo" style="left:0;top:0" width="801" height="393" viewBox="0 0 801 393" role="img" aria-label="Photo of two executives reviewing a laptop in a bright office">
    <defs><linearGradient id="p1g" x1="0" y1="0" x2="1" y2="1"><stop offset="0" stop-color="#dfe5ea"/><stop offset=".55" stop-color="#9aa8b6"/><stop offset="1" stop-color="#4d5c6b"/></linearGradient></defs>
    <polygon points="395,0 801,0 801,393 380,393 470,205" fill="url(#p1g)"/>
    <polygon points="335,0 395,0 470,205 410,205" fill="#f7a21b"/>
    <polygon points="410,205 470,205 380,393 315,393" fill="#f15a24"/>
  </svg>
  <div class="rule-orange"></div>

  <p class="copy abs" style="left:51px;top:413px;width:700px">A strong communication and marketing strategy can significantly increase the value of your business leading up to an exit. Buyers are looking to mitigate risk and unlock potential value as a catalyst for clear growth potential.</p>
  <p class="copy abs" style="left:51px;top:454px;width:700px">Highlighting your company’s success in the marketplace, identifying, and mitigating reputation risks before buyers do, enhancing employee engagement, finding hidden opportunities to boost marketing KPIs and showcasing IP, data, and innovation, can make a significant difference in valuation.</p>

  <div class="quote-box" style="left:51px;top:510px;width:338px;height:171px;padding-top:46px">
    US institutional investors believe that Investor Relations (IR) accounts for a total variance of 30% in a company’s valuation – from a premium of 10% for “superb” IR to a discount of 20% for “poor” IR.
    <div class="q-cite">–Corvane Research Group, “Measuring the Influence of IR on Enterprise Value.”</div>
  </div>
  <div class="quote-icon" style="left:197px;top:496px">“</div>

  <p class="copy abs" style="left:417px;top:515px;width:334px">We design and implement communication and marketing strategies that deliver significant increases in brand awareness, identify reputational risks, and enhance brand perception, helping owners and investors to realize premium values for their companies. We support owners and companies through:</p>

  <div class="deal-types">
    <div class="deal"><svg width="26" height="26" viewBox="0 0 26 26"><rect x="3" y="4" width="9" height="20" fill="#5aa83c"/><rect x="14" y="10" width="9" height="14" fill="#5aa83c"/><rect x="5" y="7" width="2" height="2" fill="#fff"/><rect x="8" y="7" width="2" height="2" fill="#fff"/><rect x="5" y="12" width="2" height="2" fill="#fff"/><rect x="8" y="12" width="2" height="2" fill="#fff"/></svg>Company Exit Preparation</div>
    <div class="deal"><svg width="26" height="26" viewBox="0 0 26 26"><circle cx="13" cy="13" r="11" fill="#5aa83c"/><path d="M6 14l4-3 3 2 3-3 4 3-4 4-3-2-3 2z" fill="#fff"/></svg>M&amp;A</div>
    <div class="deal"><svg width="26" height="26" viewBox="0 0 26 26"><rect x="3" y="14" width="4" height="8" fill="#5aa83c"/><rect x="9" y="10" width="4" height="12" fill="#5aa83c"/><rect x="15" y="6" width="4" height="16" fill="#5aa83c"/><rect x="21" y="3" width="3" height="19" fill="#5aa83c"/></svg>IPO</div>
    <div class="deal"><svg width="26" height="26" viewBox="0 0 26 26"><circle cx="13" cy="12" r="10" fill="#5aa83c"/><path d="M8 12l4 4 6-7" stroke="#fff" stroke-width="2.4" fill="none"/><rect x="8" y="22" width="10" height="3" fill="#5aa83c"/></svg>Spinoff/ Divestiture</div>
    <div class="deal"><svg width="26" height="26" viewBox="0 0 26 26"><circle cx="13" cy="6" r="5" fill="#5aa83c"/><path d="M4 25c0-8 4-11 9-11s9 3 9 11z" fill="#5aa83c"/></svg>New Leadership/ Investor</div>
  </div>

  <p class="copy abs" style="left:51px;top:696px;width:700px">Few sellers would list their home without first inspecting, repairing broken items, and making updates to highlight the positive aspects – increasing appeal to buyers. However, countless business owners leave money on the table during corporate exits due to a lack of preparation.</p>
  <div class="divider" style="left:51px;top:749px;width:700px"></div>

  <p class="copy abs" style="left:51px;top:780px;width:330px;font-size:10px">Our team of executive-level communications and marketing experts brings deep buy and sell-side experience. We have played critical roles in the acquisition, integration, and disposition process. Our mix of financial services expertise combined with decades of experience leading internal and external communications, marketing and investor relations teams gives us a unique perspective on identifying and unlocking non-financial areas of value and mitigating non-financial risks before exit.</p>

  <div class="orange-box" style="left:399px;top:776px;width:352px;height:112px">While accounting and investment banking teams are hard at work increasing valuation from a financial perspective, we help organizations enhance their valuation by identifying areas that will appeal most to buyers and ensuring those elements of your business are visible and memorable to those who matter most.</div>

  <h2 class="value-title" style="top:896px">We help companies increase valuation by:</h2>

  <div class="value-row">
    <div class="value-cell"><svg class="value-badge" viewBox="0 0 58 58"><polygon points="29,2 52,15 52,43 29,56 6,43 6,15" fill="#f15a24"/><circle cx="29" cy="27" r="10" fill="none" stroke="#fff" stroke-width="2.5"/><path d="M18 40h22" stroke="#fff" stroke-width="3"/></svg>Highlighting value in<br>a clear and visible way</div>
    <div class="value-cell"><svg class="value-badge" viewBox="0 0 58 58"><polygon points="29,2 52,15 52,43 29,56 6,43 6,15" fill="#5aa83c"/><circle cx="24" cy="32" r="8" fill="none" stroke="#fff" stroke-width="3"/><circle cx="36" cy="21" r="5" fill="none" stroke="#fff" stroke-width="2.5"/></svg>Streamlining the<br>exit process</div>
    <div class="value-cell"><svg class="value-badge" viewBox="0 0 58 58"><polygon points="29,2 52,15 52,43 29,56 6,43 6,15" fill="#1f7fc9"/><path d="M18 34l11-16 11 16z" fill="none" stroke="#fff" stroke-width="2.5"/><path d="M16 40h26" stroke="#fff" stroke-width="3"/></svg>Identifying potential<br>risks and suggesting<br>mitigation measures</div>
    <div class="value-cell"><svg class="value-badge" viewBox="0 0 58 58"><polygon points="29,2 52,15 52,43 29,56 6,43 6,15" fill="#f7a21b"/><circle cx="29" cy="22" r="6" fill="none" stroke="#fff" stroke-width="2.5"/><path d="M15 38h28" stroke="#fff" stroke-width="3"/><circle cx="19" cy="32" r="3" fill="#fff"/><circle cx="39" cy="32" r="3" fill="#fff"/></svg>Creating a polished<br>presence in the market<br>ahead of buyer interest</div>
  </div>

  <div class="footer" style="top:1079px">
    <span class="item"><svg width="14" height="11" viewBox="0 0 14 11"><rect x=".5" y=".5" width="13" height="10" rx="1" fill="none" stroke="#1f7fc9"/><path d="M1 1l6 5 6-5" stroke="#1f7fc9" fill="none"/></svg>info@brightmoorlane.partners</span>
    <span class="sep">|</span>
    <span class="item"><svg width="11" height="14" viewBox="0 0 11 14"><path d="M5.5 13.5C2 9 1 7 1 5a4.5 4.5 0 019 0c0 2-1 4-4.5 8.5z" fill="#1f7fc9"/><circle cx="5.5" cy="5" r="1.6" fill="#fff"/></svg>Carrowden</span>
    <span class="sep">|</span>
    <span class="item"><svg width="13" height="13" viewBox="0 0 13 13"><circle cx="6.5" cy="6.5" r="5.8" fill="none" stroke="#1f7fc9"/><path d="M.7 6.5h11.6M6.5.7c-3 3-3 8.6 0 11.6M6.5.7c3 3 3 8.6 0 11.6" stroke="#1f7fc9" fill="none"/></svg>www.brightmoorlane.partners</span>
  </div>
</section>

<section class="page page-two">
  <svg class="abs" style="left:0;top:0" width="779" height="144" viewBox="0 0 779 144" role="img" aria-label="Blue header band with a faint photo of a city skyline">
    <defs><linearGradient id="p2g" x1="0" y1="0" x2="1" y2="0"><stop offset="0" stop-color="#1565a8"/><stop offset="1" stop-color="#2f8fd6"/></linearGradient></defs>
    <polygon points="250,0 779,0 779,144 250,144 300,72" fill="url(#p2g)"/>
    <polygon points="205,0 232,0 282,72 260,72" fill="#f7a21b"/>
    <polygon points="260,72 282,72 232,144 205,144" fill="#f15a24"/>
    <polygon points="232,0 250,0 300,72 282,72" fill="#1e2c37"/>
    <polygon points="282,72 300,72 250,144 232,144" fill="#5aa83c"/>
  </svg>
  <div class="brand" style="left:51px;top:56px"><span class="brand-mark"></span><span class="brand-name">Brightmoor Lane Partners</span></div>
  <p class="banner-text">SaleNimbus provides executives and business owners with clear guidance to unlock value ahead of an exit. Our non-disruptive, ala-carte process enables us to work with sellers on specific areas or to do a complete analysis and recommendation and can include:</p>

  <h2 class="section-head blue" style="left:51px;top:153px">Brand Analysis and Recommendations</h2>
  <p class="copy abs" style="left:51px;top:180px;width:680px;font-size:10px">Strong brands command a higher valuation. We conduct a brand analysis, providing clear and detailed recommendations to enhance your value proposition and help you stand out from the crowd:</p>

  <ul class="checks" style="left:51px;top:214px;width:330px">
    <li><b>Current external position among competitors</b>We look at how your brand measures up based on external competitive analysis, positioning in the media and analyst community, and across other digital channels.</li>
    <li><b>Physical brand image</b>A little bit of paint and updated fixtures can go a long way when increasing the value of a home. The same is true for businesses. Our audit evaluates non-disruptive steps your company can take to enhance your brand look and feel before sale.</li>
  </ul>
  <ul class="checks" style="left:400px;top:214px;width:330px">
    <li><b>Employee brand perception</b>We conduct a high-level internal audit with recommendations to enhance engagement for current and prospective employees.</li>
    <li><b>Current external position among competitors</b>We conduct a high-level external audit showcasing how customers perceive your brand in the market. We then provide recommendations for enhancing engagement and maximizing value.</li>
  </ul>

  <div class="stat-box">
    <div class="stat" style="left:14px;top:12px;padding-top:12px">5%<span>increase</span></div>
    <div class="stat" style="left:76px;top:12px;padding-top:12px;font-size:17px">25%<span>increase</span></div>
    <div class="stat" style="left:14px;top:76px;padding-top:12px">5<span>times</span></div>
    <div class="stat" style="left:76px;top:76px;padding-top:12px">16<span>times</span></div>
    <p class="stat-text" style="top:16px">A <b>5% increase</b> in customer retention correlates with at least a <b>25% increase</b> in profit, according to an analysis by Halvern &amp; Company.<br><u>(https://media.halvern.example/files/HC_Prescription_cutting_costs.pdf)</u></p>
    <p class="stat-text" style="top:80px">It costs <b>5 times</b> more to acquire a new customer than to retain a current one and <b>16 times</b> more to get new customers to the same spending level as existing ones.<br><u>(https://martechdesk.example/customer-retention-guide-statistics/)</u></p>
  </div>

  <div class="dotted" style="left:75px;top:570px;height:310px"></div>
  <div class="icon-tile" style="left:57px;top:534px;background:var(--amber)"></div>
  <div class="icon-tile" style="left:57px;top:703px;background:var(--green)"></div>
  <div class="icon-tile" style="left:57px;top:876px;background:var(--blue)"></div>

  <h2 class="section-head orange" style="left:109px;top:528px">Digital and Traditional Marketing Analysis and Recommendations</h2>
  <p class="copy abs" style="left:109px;top:555px;width:625px;font-size:10px">How much money are you leaving on the table? Our marketing audits help organizations identify areas of hidden value that can have significant impacts on revenue and valuation. We optimize current activities and uncover new strategies to increase the effectiveness of current marketing spend. Areas we evaluate include:</p>
  <ul class="checks bold" style="left:109px;top:606px;width:300px">
    <li>Website traffic and conversion</li>
    <li>CRM process review to identify strategies and recommendations to increase conversion and reactive old-leads</li>
    <li>Email marketing strategy</li>
  </ul>
  <ul class="checks bold" style="left:450px;top:606px;width:280px">
    <li>Automations and drip marketing</li>
    <li>Social media strategy /presence</li>
    <li>Partnership marketing</li>
    <li>Paid media analysis/strategy suggestion</li>
  </ul>

  <h2 class="section-head orange" style="left:109px;top:697px">Messaging and Content Strategy Review and Analysis</h2>
  <p class="copy abs" style="left:109px;top:724px;width:625px;font-size:10px">It’s about your valuation. Full and fair valuation requires a clear, compelling investment case articulated consistently to the right audience at the right time. Messaging to maximize your value in an acquisition or an IPO is quite different from typical selling messages for prospects, customers, or ‘features &amp; business benefits’ for press and analysts. We understand the issues and speak the right language to maximize perception of value with key decision makers.</p>
  <ul class="checks bold" style="left:109px;top:785px;width:310px">
    <li>Review and recommendations of key messaging and value proposition</li>
    <li>Analysis and recommendations to position key executives likely to remain with the company as thought leaders to help build value</li>
  </ul>
  <ul class="checks bold" style="left:450px;top:785px;width:285px">
    <li>Analysis and recommendations to highlight data, IP, and innovation</li>
    <li>Analysis and recommendations to build employee engagement and retention enhancing your most valuable asset—your team</li>
  </ul>

  <h2 class="section-head orange" style="left:109px;top:870px">Media and Analyst Strategy Development</h2>
  <p class="copy abs" style="left:109px;top:896px;width:625px;font-size:10px">Positive articles and inclusion in analyst reports pack a powerful punch when preparing your business for sale. We work with clients to develop a media strategy that goes beyond brand awareness, leveraging media to build a digital history of third-party validation targeted to enhance appeal to prospective buyers while generating traffic and connections, to enhance overall value.</p>
  <ul class="checks bold" style="left:109px;top:961px;width:310px">
    <li>Positioning to media and analyst community creating third party market validation</li>
    <li>Key angle recommendations</li>
  </ul>
  <ul class="checks bold" style="left:450px;top:961px;width:285px">
    <li>Announcement timeline and strategy planning to maximize media value of news<br><span style="font-weight:500">• What is newsworthy<br>• How to position that news for the most significant impact</span></li>
  </ul>

  <div class="footer" style="top:1046px">
    <span class="item"><svg width="14" height="11" viewBox="0 0 14 11"><rect x=".5" y=".5" width="13" height="10" rx="1" fill="none" stroke="#1f7fc9"/><path d="M1 1l6 5 6-5" stroke="#1f7fc9" fill="none"/></svg>info@brightmoorlane.partners</span>
    <span class="sep">|</span>
    <span class="item"><svg width="11" height="14" viewBox="0 0 11 14"><path d="M5.5 13.5C2 9 1 7 1 5a4.5 4.5 0 019 0c0 2-1 4-4.5 8.5z" fill="#1f7fc9"/><circle cx="5.5" cy="5" r="1.6" fill="#fff"/></svg>Carrowden</span>
    <span class="sep">|</span>
    <span class="item"><svg width="13" height="13" viewBox="0 0 13 13"><circle cx="6.5" cy="6.5" r="5.8" fill="none" stroke="#1f7fc9"/><path d="M.7 6.5h11.6M6.5.7c-3 3-3 8.6 0 11.6M6.5.7c3 3 3 8.6 0 11.6" stroke="#1f7fc9" fill="none"/></svg>www.brightmoorlane.partners</span>
  </div>
</section>

<section class="page page-three">
  <div class="brand" style="left:51px;top:62px"><span class="brand-mark"></span><span class="brand-name">Brightmoor Lane Partners</span></div>
  <svg class="abs" style="left:0;top:0" width="792" height="160" viewBox="0 0 792 160" role="img" aria-label="Photo of a business team meeting around a table">
    <defs><linearGradient id="p3g" x1="0" y1="0" x2="1" y2="0"><stop offset="0" stop-color="#c8cfd6"/><stop offset=".5" stop-color="#7d8a97"/><stop offset="1" stop-color="#aab4be"/></linearGradient></defs>
    <polygon points="250,160 320,0 358,0 288,160" fill="#f15a24"/>
    <polygon points="372,0 792,0 792,160 302,160" fill="url(#p3g)"/>
  </svg>

  <div class="grey-box">
    <h3>“White Hat/Black Hat Review”</h3>
    <p class="copy" style="font-size:10.4px">We take a buyer’s communications and marketing approach to analyzing the client company and provide a “punch list” of things a potential buyer is likely to ask/request in due diligence from a comms/culture/marketing/reputation standpoint to ensure that when potential buyers start screening for sellers and evaluating them, the client company has the upper hand.</p>
  </div>

  <div class="quote-box" style="left:51px;top:363px;width:335px;height:104px;padding-top:34px">
    Strategy without tactics is the slowest route to victory. Tactics without strategy is the noise before defeat
    <div class="q-cite" style="margin-top:8px">– Ardan Vell</div>
  </div>
  <div class="quote-icon" style="left:195px;top:339px">“</div>

  <p class="lead-blue">Once the analysis is complete, we deliver actionable intelligence and recommendations to help leaders identify and quickly unlock areas that will boost value and appeal to prospective buyers. Work products include:</p>

  <div class="photo" style="left:51px;top:473px;width:345px;height:264px;background:linear-gradient(135deg,#e6e9ec,#9aa6b2 60%,#5d6b79)" role="img" aria-label="Photo of colleagues working on laptops at a shared desk"></div>

  <div class="product">
    <div class="icon-tile" style="left:448px;top:495px;background:var(--amber)"></div>
    <h4 style="left:488px;top:489px">Gap Assessment -</h4>
    <p class="copy abs" style="left:488px;top:520px;width:262px;font-size:10px">We provide a comprehensive seller report providing analysis and actionable recommendations to increase your valuation while identifying and mitigating non-financial risks.</p>
    <div class="icon-tile" style="left:448px;top:599px;background:var(--green)"></div>
    <h4 style="left:488px;top:592px">Strategic Roadmap -</h4>
    <p class="copy abs" style="left:488px;top:620px;width:262px;font-size:10px;text-align:justify">Clients are given an actionable tactical roadmap based on the recommendation provided. Organizations can choose to implement key areas or include this powerful guide as part of their presentation to prospective buyers to highlight latent potential. The roadmap provides actionable steps buyers can take upon close as they make their case for your business with their investment committees.</p>
  </div>

  <p class="note" style="top:782px"><em>Once the strategy integration</em> <b style="font-weight:500">roadmap</b> <em>is complete, your team can implement it on your timeline, we can work with your team</em> providing guidance and executive-level support, or we can fully execute deliverables with our robust capabilities and team.</p>
  <div class="dots" style="top:822px"></div>
  <p class="note" style="top:843px"><b>Our value proposition,</b> <em>based on delivering outcomes rather than just outputs, means that you receive the benefit and capability</em> of deeply experienced corporate communications leaders without adding headcount or the time to identify, recruit, onboard and retain a new team member.</p>
  <div class="dots" style="top:896px"></div>
  <p class="note" style="top:922px"><b>We help organizations enhance</b> <em>their valuation by identifying areas that will appeal most to buyers and ensuring those ele-</em> ments of your business are visible and memorable to those who matter most.</p>
  <div class="dots" style="top:958px"></div>
  <p class="note" style="top:984px"><b>SaleNimbus helps sellers maximize valuation</b> <em>and unlock hidden potential ahead of an exit—ensuring money is not left</em> on the table.</p>
  <div class="dots" style="top:1026px"></div>

  <div class="footer" style="top:1064px">
    <span class="item"><svg width="14" height="11" viewBox="0 0 14 11"><rect x=".5" y=".5" width="13" height="10" rx="1" fill="none" stroke="#1f7fc9"/><path d="M1 1l6 5 6-5" stroke="#1f7fc9" fill="none"/></svg>info@brightmoorlane.partners</span>
    <span class="sep">|</span>
    <span class="item"><svg width="11" height="14" viewBox="0 0 11 14"><path d="M5.5 13.5C2 9 1 7 1 5a4.5 4.5 0 019 0c0 2-1 4-4.5 8.5z" fill="#1f7fc9"/><circle cx="5.5" cy="5" r="1.6" fill="#fff"/></svg>Carrowden</span>
    <span class="sep">|</span>
    <span class="item"><svg width="13" height="13" viewBox="0 0 13 13"><circle cx="6.5" cy="6.5" r="5.8" fill="none" stroke="#1f7fc9"/><path d="M.7 6.5h11.6M6.5.7c-3 3-3 8.6 0 11.6M6.5.7c3 3 3 8.6 0 11.6" stroke="#1f7fc9" fill="none"/></svg>www.brightmoorlane.partners</span>
  </div>
</section>

</body>
</html>
```